Tarnby Group letterhead

Hi,

I need a letterhead template created for our business. This should be done in word format and A4 size. The images need to not move in the template ie when I am adding writing in etc. and should flow on when I get to a second page.

I have attached our logo templates below.

Other details to include on the letterhead somewhere are:

0438 915 267
Max@Tarnbyelectrical.example.au
PO Box 817 Marrowvale NSW 2190
ABN: 57 318 962 407

Thanks!

```html
<!DOCTYPE html>
<html lang="en">
<head>
<meta charset="utf-8">
<title>Tarnby Group Letterhead</title>
<link href="https://fonts.googleapis.com/css2?family=Lato:wght@400;700;900&family=Montserrat:wght@300;400&display=swap" rel="stylesheet">
<style>
  :root {
    --backdrop: #e6e6e8;
    --paper: #ffffff;
    --ink: #231f20;
    --band: #1c1c1c;
    --accent: #f05423;
    --faint: #f3f0ee;
    --footer-text: #e8e8e8;
  }
  * { margin: 0; padding: 0; box-sizing: border-box; }
  html, body {
    width: 1200px; height: 960px; overflow: hidden;
    background: var(--backdrop);
  }
  .letterhead {
    position: absolute; left: 260px; top: 20px;
    width: 680px; height: 920px;
    background: var(--paper);
    box-shadow: 0 6px 24px rgba(0,0,0,0.15);
    overflow: hidden;
    font-family: "Lato", sans-serif;
    color: var(--ink);
  }
  .faint-ring {
    position: absolute; left: 300px; top: -40px;
    width: 230px; height: 230px;
    border: 18px solid var(--faint); border-radius: 50%;
  }
  .brand {
    position: absolute; left: 52px; top: 46px;
    display: flex; align-items: center; gap: 12px;
  }
  .brand-circle {
    width: 46px; height: 46px; border-radius: 50%;
    border: 5px solid var(--ink);
  }
  .brand-name {
    font-weight: 900; font-size: 26px; letter-spacing: 1px;
    text-transform: uppercase; color: var(--ink);
  }
  .letter {
    position: absolute; left: 60px; top: 150px; width: 520px;
    font-size: 11.5px; line-height: 1.45;
  }
  .letter-date { margin-bottom: 12px; }
  .recipient { margin-bottom: 12px; }
  .salutation { font-weight: 700; font-size: 15px; margin: 16px 0 10px; }
  .letter p.body { margin-bottom: 14px; }
  .sign-off { margin-top: 18px; }
  .footer-wave {
    position: absolute; left: 0; top: 0; width: 680px; height: 920px;
  }
  .footer-contact {
    position: absolute; bottom: 24px; left: 60px; right: 30px;
    display: flex; align-items: center; gap: 18px;
    font-family: "Montserrat", sans-serif; font-weight: 300;
    font-size: 11px; line-height: 1.6; color: var(--footer-text);
  }
  .contact-line { display: flex; align-items: center; gap: 6px; }
  .contact-line svg { width: 10px; height: 10px; fill: var(--accent); }
  .footer-divider { width: 1px; height: 30px; background: var(--accent); }
  .abn-label { color: var(--accent); }
</style>
</head>
<body>
  <main class="letterhead">
    <div class="faint-ring" aria-hidden="true"></div>

    <header class="brand">
      <span class="brand-circle" aria-hidden="true"></span>
      <span class="brand-name">Tarnby Group</span>
    </header>

    <section class="letter">
      <p class="letter-date">January-03-2020</p>
      <p class="recipient">Mr. John Doe<br>President</p>
      <p class="recipient">Link Corpporation<br>123 Street Name, Suite# 10<br>City, State, 120023</p>
      <p class="salutation">Dear Mr. John</p>
      <p class="body">Lorem ipsum dolor sit amet, consectetur adipiscing elit, sed do eiusmod tempor incididunt ut labore et dolore magna aliqua. Ut enim ad minim veniam, quis nostrud exercitation ullamco laboris nisi ut aliquip ex ea commodo consequat. Duis aute irure dolor in reprehenderit in voluptate velit esse cillum dolore eu fugiat nulla pariatur.</p>
      <p class="body">Lorem ipsum dolor sit amet, consectetur adipiscing elit, sed do eiusmod tempor incididunt ut labore et dolore magna aliqua. Ut enim ad minim veniam, quis nostrud exercitation ullamco laboris nisi ut aliquip ex ea commodo consequat. Duis aute irure dolor in reprehenderit in voluptate velit esse cillum dolore eu fugiat nulla pariatur.</p>
      <p class="body">Lorem ipsum dolor sit amet, consectetur adipiscing elit, sed do eiusmod tempor incididunt ut labore et dolore magna aliqua. Ut enim ad minim veniam, quis nostrud exercitation ullamco laboris nisi ut aliquip ex ea commodo consequat.</p>
      <p class="body">Excepteur sint occaecat cupidatat non proident, sunt in culpa qui officia deserunt mollit anim id est laborum. re et dolore magnam aliquam quaerat voluptatem.</p>
      <p class="sign-off">Regards</p>
    </section>

    <svg class="footer-wave" viewBox="0 0 680 920" aria-hidden="true">
      <path d="M300 742 C 400 692, 540 602, 680 555 L680 578 C 560 614, 430 684, 300 742 Z" fill="var(--accent)"/>
      <path d="M30 824 C 215 814, 335 724, 462 660 C 550 616, 620 594, 680 584" fill="none" stroke="var(--accent)" stroke-width="4"/>
      <path d="M0 842 C 200 832, 330 742, 460 677 C 550 632, 620 612, 680 602 L680 920 L0 920 Z" fill="var(--band)"/>
    </svg>

    <footer class="footer-contact">
      <div class="contact-group">
        <p class="contact-line">
          <svg viewBox="0 0 24 24"><path d="M6.6 10.8a15 15 0 0 0 6.6 6.6l2.2-2.2a1 1 0 0 1 1-.25 11.4 11.4 0 0 0 3.6.57 1 1 0 0 1 1 1V20a1 1 0 0 1-1 1A17 17 0 0 1 3 4a1 1 0 0 1 1-1h3.5a1 1 0 0 1 1 1c0 1.25.2 2.450.57 3.570a1 1 0 0 1-.25 1Z"/></svg>
          0438 915 267
        </p>
        <p class="contact-line">
          <svg viewBox="0 0 24 24"><path d="M2 5h20v14H2Zm2 2v.5l8 5 8-5V7l-8 5Z"/></svg>
          Max@Tarnbyelectrical.example.au
        </p>
      </div>
      <span class="footer-divider" aria-hidden="true"></span>
      <div class="contact-group">
        <p>PO Box 817 Marrowvale NSW 2190</p>
        <p><span class="abn-label">ABN:</span> 57 318 962 407</p>
      </div>
    </footer>
  </main>
</body>
</html>
```